Develop website for Cloud Security Startup

Looking for a logo that conveys the outsourced security and management of clients data, systems and development in Tessora, Kfn and Brintel with an emphasis on security and compliance

Target Market(s)

Companies looking for professional services IT firm

Coding

Coded - Design and coding required

Number of Pages Required

5+ page

Font styles to use
Sans Serif

Colors
0455a3
33a6d7

Requirements
Must have
• Landing Page
- Help me get started

Move to the cloud safely
- Benefits of Cloud

What we do
- Cloud Adoption
- Managed Services
- Optimise

Resources
- News
- Resources
- Events
- Webinars
- Not for profit
- Case Studies
- Support Button
- Incident Button

Company
- About Us
- Why Vorselith?
- Acreditations
- Halvendor Tessora Partner
- Net Promoter Score
- Careers
- Contact Us

Contact Us

```html
<!DOCTYPE html>
<html lang="en">
<head>
<meta charset="utf-8">
<title>Vorselith – Effective Technology Management</title>
<link href="https://fonts.googleapis.com/css2?family=Oswald:wght@400;500;600&family=Open+Sans:wght@400;600;700&display=swap" rel="stylesheet">
<style>
:root{
  --brand:#0455a3;
  --brand-light:#33a6d7;
  --brand-dark:#0a3a85;
  --ink:#1b1f2a;
  --muted:#4a4f5c;
  --soft:#eef1f5;
  --white:#ffffff;
}
*{box-sizing:border-box;margin:0;padding:0}
html,body{width:1200px;height:5172px;overflow:hidden}
body{position:relative;font-family:'Open Sans',Arial,sans-serif;color:var(--ink);background:var(--white)}
.abs{position:absolute}
.head{font-family:'Oswald','Arial Narrow',sans-serif;font-weight:500;text-transform:uppercase}
.btn{position:absolute;display:flex;align-items:center;justify-content:center;font-size:14px;font-weight:700;text-transform:uppercase;border-radius:4px}
.btn-blue{background:var(--brand);color:var(--white);box-shadow:0 3px 0 var(--brand-dark)}
.btn-white{background:var(--white);color:var(--brand)}
.divider{position:absolute;width:100px;height:24px;left:50%;margin-left:-50px}
.divider::before{content:"";position:absolute;top:11px;left:0;right:0;height:2px;background:var(--brand)}
.divider::after{content:"";position:absolute;left:40px;top:0;width:20px;height:20px;border-radius:50% 50% 50% 0;transform:rotate(-45deg);background:var(--brand);box-shadow:inset 0 0 0 6px var(--brand),inset 0 0 0 10px var(--white)}
.divider.left{left:100px;margin-left:0}
.divider.light::before{background:var(--white)}
.divider.light::after{background:var(--white);box-shadow:inset 0 0 0 6px var(--white),inset 0 0 0 10px var(--brand)}

/* header */
.topbar{left:440px;top:0;width:760px;height:36px;background:var(--brand-light);color:var(--white);font-size:14px;display:flex;align-items:center;padding-left:30px;gap:48px}
.topbar .social{margin-left:auto;display:flex;gap:18px;padding-right:50px}
.topbar .social span{width:14px;height:14px;border-radius:3px;background:rgba(255,255,255,.85)}
.logo{left:100px;top:6px;display:flex;align-items:center;gap:12px}
.logo .mark{width:56px;height:56px;border-radius:50%;background:var(--brand)}
.logo .word{font-size:28px;font-weight:700;color:var(--brand);line-height:1}
.logo .tag{font-size:9px;font-weight:600;color:var(--brand);display:block;margin-top:3px}
.nav{top:54px;left:390px;display:flex;font-size:14px;font-weight:700;color:var(--ink)}
.nav a{color:inherit;text-decoration:none;position:absolute;white-space:nowrap}
.nav a.active{color:var(--brand-light)}

/* hero */
.hero{left:0;top:88px;width:1200px;height:582px;background:linear-gradient(90deg,#5f7585 0%,#8ea1ae 45%,#c7d2da 70%,#8c9aa4 100%)}
.hero h1{position:absolute;left:100px;top:190px;font-size:46px;line-height:50px;color:var(--white);font-family:'Oswald',sans-serif;font-weight:500;text-transform:uppercase}
.hero p{position:absolute;left:100px;top:300px;width:450px;font-size:13px;line-height:22px;color:var(--white)}
.hero .arrow{position:absolute;top:272px;width:20px;height:20px;border-left:2px solid var(--white);border-bottom:2px solid var(--white)}
.dots{position:absolute;display:flex;gap:10px}
.dots i{width:10px;height:10px;border-radius:50%;border:2px solid var(--white)}
.dots i.on{background:var(--white)}

/* band */
.band{left:0;top:670px;width:1200px;height:185px;background:var(--brand);border-bottom-right-radius:140px}
.band h2{position:absolute;left:167px;top:70px;font-size:36px;color:var(--white)}

/* benefits */
.benefits{left:0;top:855px;width:1200px;height:740px;background:linear-gradient(135deg,#f3f5f8,#e6eaef);border-bottom-left-radius:160px}
.title{position:absolute;width:100%;text-align:center;font-size:44px;color:var(--ink)}
.orbit{position:absolute;left:370px;top:185px;width:450px;height:450px;border:2px dotted var(--brand-light);border-radius:50%}
.core{position:absolute;left:485px;top:300px;width:220px;height:220px;border-radius:50%;background:#d3e1ec;display:flex;align-items:center;justify-content:center}
.core span{width:150px;height:150px;border-radius:50%;background:var(--white);display:flex;align-items:center;justify-content:center}
.core span b{width:80px;height:80px;border-radius:50%;background:var(--brand)}
.node{position:absolute;width:72px;height:72px;border-radius:50%;background:var(--white);box-shadow:0 4px 14px rgba(4,85,163,.18);display:flex;align-items:center;justify-content:center}
.node svg{width:34px;height:34px;stroke:var(--brand-light);fill:none;stroke-width:2}
.blabel{position:absolute;font-size:17px;line-height:24px;color:var(--ink)}
.blabel.r{text-align:right}

/* services */
.svc-img{position:absolute;width:315px;height:370px;border-top-right-radius:40px}
.svc-badge{position:absolute;width:62px;height:62px;background:var(--white);display:flex;align-items:center;justify-content:center}
.svc-badge svg{width:36px;height:36px;stroke:var(--brand);fill:none;stroke-width:2}
.svc-title{position:absolute;font-size:30px;font-weight:600;color:var(--brand-light)}
.svc-text{position:absolute;width:315px;font-size:17px;line-height:26px;color:var(--muted)}
.city{left:0;top:2330px;width:1200px;height:270px;background:linear-gradient(180deg,#ffffff 0%,#d9e0e6 45%,#7d8c99 100%)}

/* experience */
.experience{left:0;top:2600px;width:1200px;height:710px;background:linear-gradient(90deg,#f6f7f9,#eef1f4);border-top-right-radius:160px}
.exp-title{position:absolute;left:100px;top:115px;font-family:'Oswald',sans-serif;font-weight:400;font-size:46px;line-height:56px;color:var(--ink)}
.exp-title b{font-weight:600}
.exp-copy{position:absolute;left:100px;top:345px;width:470px;font-size:14px;line-height:29px;color:var(--muted)}
.card{position:absolute;width:207px;background:var(--white);border-top-right-radius:26px;box-shadow:0 4px 18px rgba(0,0,0,.08);padding:22px 22px}
.card svg{width:44px;height:44px;stroke:var(--brand-light);fill:none;stroke-width:2;display:block}
.card h3{font-size:18px;font-weight:400;color:var(--brand-light);line-height:22px;margin:8px 0 8px}
.card-text{font-size:10px;line-height:17px;color:var(--muted)}
.card.blue{background:linear-gradient(180deg,#1e62b8,var(--brand-dark))}
.card.blue h3,.card.blue .card-text{color:var(--white)}
.card.blue svg{stroke:var(--white)}

/* testimonial */
.testi{left:0;top:3310px;width:1200px;height:630px;background:linear-gradient(180deg,#063f95,#0a5cb8);border-bottom-left-radius:160px}
.quote{position:absolute;top:200px;width:318px;height:235px;background:var(--white);padding:30px 20px}
.quote::after{content:"";position:absolute;left:30px;bottom:-14px;border:14px solid transparent;border-top-color:var(--white);border-bottom:0}
.quote .qm{font-family:'Oswald',sans-serif;font-size:54px;line-height:30px;color:var(--brand);font-weight:600}
.quote p{font-size:14px;line-height:22px;font-style:italic;color:var(--muted);margin-top:12px}
.person{position:absolute;top:458px;display:flex;align-items:center;gap:10px;color:var(--white);font-size:13px;font-weight:700}
.person i{width:36px;height:36px;border-radius:50%;background:#c9d4df}
.person small{display:block;color:#f4c430;font-size:10px;letter-spacing:1px}

/* contact */
.contact-intro{position:absolute;left:0;top:4125px;width:1200px;text-align:center;font-size:15px;line-height:26px;color:var(--muted)}
.info{position:absolute;top:4238px;font-size:14px;line-height:22px;color:var(--muted)}
.info b{display:block;font-weight:400;color:var(--brand-light);font-size:15px}
.footer{left:0;top:4690px;width:1200px;height:482px;background:linear-gradient(180deg,#063f95,#0b4aa5)}
.form{left:145px;top:4350px;width:455px;height:440px;background:var(--brand-dark);border-top-left-radius:40px;padding:0 30px}
.field{position:absolute;border-bottom:1px solid rgba(255,255,255,.6);color:var(--white);font-size:12px;height:30px}
.field::after{content:"*";position:absolute;right:4px;top:0}
.map{left:600px;top:4350px;width:453px;height:440px;background:linear-gradient(135deg,#eef0f2,#dde2e7);border-bottom-right-radius:40px}
.fhead{position:absolute;top:4882px;font-size:15px;font-weight:700;color:var(--white)}
.flinks{position:absolute;top:4918px;font-size:14px;line-height:29px;color:var(--white);list-style:none}
.fsocial{position:absolute;top:5075px;width:36px;height:36px;border:1px solid rgba(255,255,255,.7)}
</style>
</head>
<body>

<!-- header -->
<div class="abs topbar"><span>Phone : 555 014 2270</span><span>Email : info@vorselith.com</span><span class="social"><span></span><span></span><span></span><span></span></span></div>
<div class="abs logo"><span class="mark"></span><span><span class="word">VORSELITH</span><span class="tag">EFFECTIVE TECHNOLOGY MANAGEMENT</span></span></div>
<nav class="abs nav">
  <a class="active" style="left:0">HOME</a>
  <a style="left:115px">WHAT WE DO ⌄</a>
  <a style="left:290px">RESOURCES ⌄</a>
  <a style="left:465px">COMANY ⌄</a>
  <a style="left:615px">CONTACT US</a>
</nav>

<!-- hero -->
<section class="abs hero" role="img" aria-label="Businessman touching a glowing security shield surrounded by network nodes and cloud provider icons">
  <span class="arrow" style="left:58px;transform:rotate(45deg)"></span>
  <span class="arrow" style="left:1120px;transform:rotate(-135deg)"></span>
  <h1>Vorselith Effective<br>Technology Management</h1>
  <p>Lorem ipsum dolor sit amet, consectetur adipiscing elit, sed do eiusmod tempor incididunt ut labore et dolore magna aliqua</p>
  <div class="btn btn-blue" style="left:100px;top:372px;width:168px;height:48px">Get Started</div>
  <div class="dots" style="left:558px;top:536px"><i class="on"></i><i></i><i></i><i></i></div>
</section>

<!-- band -->
<section class="abs band">
  <h2 class="head">Progression, your IT service provider</h2>
  <div class="btn btn-white" style="left:862px;top:70px;width:168px;height:48px">Get in touch</div>
</section>

<!-- benefits -->
<section class="abs benefits">
  <h2 class="title head" style="top:50px">Our Benefits</h2>
  <span class="divider" style="top:118px"></span>
  <div class="orbit"></div>
  <div class="core"><span><b></b></span></div>

  <div class="node" style="left:419px;top:204px"><svg viewBox="0 0 34 34"><path d="M9 24a6 6 0 0 1 1-12 8 8 0 0 1 15 2 5 5 0 0 1 0 10z"/></svg></div>
  <div class="node" style="left:689px;top:204px"><svg viewBox="0 0 34 34"><circle cx="15" cy="15" r="9"/><path d="M22 22l7 7"/></svg></div>
  <div class="node" style="left:352px;top:319px"><svg viewBox="0 0 34 34"><rect x="7" y="4" width="18" height="24"/><path d="M11 11h10M11 16h10M11 21h6"/></svg></div>
  <div class="node" style="left:764px;top:319px"><svg viewBox="0 0 34 34"><rect x="9" y="4" width="16" height="26" rx="2"/><path d="M13 16l3 3 5-6"/></svg></div>
  <div class="node" style="left:344px;top:431px"><svg viewBox="0 0 34 34"><rect x="5" y="7" width="24" height="21" rx="2"/><path d="M5 13h24M12 4v6M22 4v6"/></svg></div>
  <div class="node" style="left:764px;top:431px"><svg viewBox="0 0 34 34"><rect x="7" y="4" width="18" height="24"/><path d="M11 20v4M16 15v9M21 11v13"/></svg></div>
  <div class="node" style="left:422px;top:554px"><svg viewBox="0 0 34 34"><circle cx="17" cy="17" r="5"/><path d="M17 4v5M17 25v5M4 17h5M25 17h5M8 8l4 4M22 22l4 4M8 26l4-4M22 12l4-4"/></svg></div>
  <div class="node" style="left:682px;top:554px"><svg viewBox="0 0 34 34"><circle cx="17" cy="17" r="12"/><circle cx="17" cy="17" r="7"/><circle cx="17" cy="17" r="2"/></svg></div>

  <div class="blabel r" style="left:290px;top:200px;width:98px">Cloud<br>Security</div>
  <div class="blabel" style="left:797px;top:200px">Security<br>Analytics</div>
  <div class="blabel r" style="left:160px;top:316px;width:148px">Regulatory<br>Compliance</div>
  <div class="blabel" style="left:871px;top:316px">Intrusion<br>Detection</div>
  <div class="blabel r" style="left:160px;top:431px;width:148px">Incident<br>Response</div>
  <div class="blabel" style="left:871px;top:431px">Log Data<br>Analysis</div>
  <div class="blabel r" style="left:200px;top:554px;width:180px">Configuration<br>Assessment</div>
  <div class="blabel" style="left:791px;top:554px">File Integrity<br>Monitoring</div>
</section>

<!-- services -->
<div class="svc-img" style="left:95px;top:1690px;background:linear-gradient(135deg,#0c2347,#2d6ab0 60%,#7fb0da)" role="img" aria-label="Businessman with a digital globe and cloud network graphics"></div>
<div class="svc-badge" style="left:348px;top:2000px"><svg viewBox="0 0 36 36"><path d="M10 16a5 5 0 0 1 1-10 7 7 0 0 1 13 2 4 4 0 0 1 1 8z"/><rect x="10" y="20" width="16" height="5"/><rect x="10" y="27" width="16" height="5"/></svg></div>
<div class="svc-title" style="left:95px;top:2082px">Cloud Adoption</div>
<div class="svc-text" style="left:95px;top:2132px">Lorem ipsum r sit amet, consectetur adipiscing elit, sed do eiusod tempor incididunt ut labore</div>

<div class="svc-img" style="left:440px;top:1745px;background:linear-gradient(135deg,#3a4654,#7d8b99 55%,#b7c2cc)" role="img" aria-label="Businessman presenting managed service icons"></div>
<div class="svc-badge" style="left:693px;top:2055px"><svg viewBox="0 0 36 36"><path d="M8 18a5 5 0 0 1 1-10 8 8 0 0 1 15 2 4 4 0 0 1 1 8z"/><path d="M12 18v12M18 18v12M24 18v12"/></svg></div>
<div class="svc-title" style="left:440px;top:2140px">Managed Services</div>
<div class="svc-text" style="left:440px;top:2190px">Lorem ipsum r sit amet, consectetur adipiscing elit, sed do eiusod tempor incididunt ut labore</div>

<div class="svc-img" style="left:783px;top:1810px;background:linear-gradient(135deg,#e7b76d,#6f7f8e 50%,#3c4652)" role="img" aria-label="Hand pointing at optimisation gear graphics on a screen"></div>
<div class="svc-badge" style="left:1036px;top:2120px"><svg viewBox="0 0 36 36"><circle cx="18" cy="18" r="6"/><path d="M18 5v5M18 26v5M5 18h5M26 18h5M9 9l4 4M23 23l4 4M9 27l4-4M23 13l4-4"/></svg></div>
<div class="svc-title" style="left:783px;top:2204px">Optimise</div>
<div class="svc-text" style="left:783px;top:2254px">Lorem ipsum r sit amet, consectetur adipiscing elit, sed do eiusod tempor incididunt ut labore</div>

<div class="abs city" role="img" aria-label="City skyline rising above the clouds"></div>

<!-- experience -->
<section class="abs experience">
  <h2 class="exp-title">Years of experience<br>in <b>IT support and<br>development</b></h2>
  <span class="divider left" style="top:297px"></span>
  <p class="exp-copy">Lorem ipsum dolor sit amet, consectetur adipng elit, sed do eiusmod tempor incididunt ut labua. Quis ipsum suspendisse ultrices gravida. Risus commodo viverra maecenasn lacus vel facilisis. Lorem ipsum dolor sit amet, consectetur ad elit, sed do eiusmod tempor incididunt ut labua. Quis ipsum suspendisse ultrices gravida.</p>
  <div class="btn btn-blue" style="left:100px;top:530px;width:168px;height:46px">Contact us</div>

  <div class="card" style="left:625px;top:72px;height:228px"><svg viewBox="0 0 44 44"><circle cx="22" cy="18" r="9"/><path d="M16 26l-3 12 9-5 9 5-3-12"/></svg><h3>Halvendor Certified Engineers</h3><div class="card-text">Lorem ipsum dolor it crsectetur adipiscing elit, sed do eiusmod tempor incididunt Lorem ipsum dolor it amet, crsectetur</div></div>
  <div class="card" style="left:625px;top:325px;height:228px"><svg viewBox="0 0 44 44"><path d="M22 6a12 12 0 0 1 7 22v6H15v-6A12 12 0 0 1 22 6z"/><path d="M17 38h10"/></svg><h3>Experience<br>Center</h3><div class="card-text">Lorem ipsum dolor it crsectetur adipiscing elit, sed do eiusmod tempor incididunt Lorem ipsum dolor it amet, crsectetur</div></div>
  <div class="card blue" style="left:860px;top:158px;height:222px"><svg viewBox="0 0 44 44"><circle cx="20" cy="22" r="14"/><path d="M20 14v8l6 4"/></svg><h3>24/7 Professional Support</h3><div class="card-text">Lorem ipsum dolor it crsectetur adipiscing elit, sed do eiusmod tempor incididunt Lorem ipsum dolor it amet, crsectetur</div></div>
  <div class="card" style="left:860px;top:408px;height:227px"><svg viewBox="0 0 44 44"><circle cx="22" cy="22" r="7"/><path d="M22 6v7M22 31v7M6 22h7M31 22h7"/></svg><h3>Business Process Consulting</h3><div class="card-text">Lorem ipsum dolor it crsectetur adipiscing elit, sed do eiusmod tempor incididunt Lorem ipsum dolor it amet, crsectetur</div></div>
</section>

<!-- testimonial -->
<section class="abs testi">
  <h2 class="title head" style="top:75px;color:var(--white)">Testimonial</h2>
  <span class="divider light" style="top:140px"></span>
  <div class="quote" style="left:100px"><div class="qm">“</div><p>Lorem ipsum dolor sir adipiscing elit, sed do eiusmod tr incididunt ut lore et dolore magna aliqua. Quis ipsum susse ultrices gravida. Risus commodo virra maecenas accumsan lacus vel facilisis. Lorem ipsum dolor sir adipiscing elit, sed</p></div>
  <div class="quote" style="left:440px"><div class="qm">“</div><p>Lorem ipsum dolor sir adipiscing elit, sed do eiusmod tr incididunt ut lore et dolore magna aliqua. Quis ipsum susse ultrices gravida. Risus commodo virra maecenas accumsan lacus vel facilisis. Lorem ipsum dolor sir adipiscing elit, sed</p></div>
  <div class="quote" style="left:780px"><div class="qm">“</div><p>Lorem ipsum dolor sir adipiscing elit, sed do eiusmod tr incididunt ut lore et dolore magna aliqua. Quis ipsum susse ultrices gravida. Risus commodo virra maecenas accumsan lacus vel facilisis. Lorem ipsum dolor sir adipiscing elit, sed</p></div>
  <div class="person" style="left:122px"><i></i><span>JOHN DOE<small>★★★★★</small></span></div>
  <div class="person" style="left:462px"><i></i><span>JOHN DOE<small>★★★★★</small></span></div>
  <div class="person" style="left:802px"><i></i><span>JOHN DOE<small>★★★★★</small></span></div>
  <div class="dots" style="left:560px;top:535px"><i style="width:8px;height:8px;border:0;background:rgba(255,255,255,.6)"></i><i style="width:8px;height:8px;border:0;background:rgba(255,255,255,.6)"></i><i style="width:10px;height:10px;border:0;background:var(--white)"></i><i style="width:8px;height:8px;border:0;background:rgba(255,255,255,.6)"></i><i style="width:8px;height:8px;border:0;background:rgba(255,255,255,.6)"></i></div>
</section>

<!-- contact -->
<h2 class="title head" style="top:4020px">Feel free to contact us</h2>
<span class="divider" style="top:4090px"></span>
<p class="contact-intro">Lorem ipsum dolor sit amet, consectetur adipiscing elit, sed do eiusmod<br>tempor incididunt ut labore et dolore magna aliqua.</p>
<div class="abs head" style="left:150px;top:4240px;font-size:26px;color:var(--ink);border-bottom:2px solid var(--brand);line-height:32px">Get in touch</div>
<div class="info" style="left:412px"><b>ADDRESS:</b>48 Lumen Row Harbury<br>USA 30418</div>
<div class="info" style="left:705px"><b>TELEPHONE:</b>(555) 014 2270</div>
<div class="info" style="left:918px"><b>EMAIL:</b>info@vorselith.com</div>

<footer class="abs footer"></footer>
<div class="abs form">
  <div class="field" style="left:30px;top:108px;width:170px">YOUR NAME</div>
  <div class="field" style="left:238px;top:108px;width:188px">EMAIL ADDRESS</div>
  <div class="field" style="left:30px;top:190px;width:170px">PHONE</div>
  <div class="field" style="left:238px;top:190px;width:188px">TOPIC</div>
  <div class="field" style="left:30px;top:258px;width:396px;height:95px">YOUR MESSAGE</div>
  <div class="btn btn-white" style="left:32px;top:384px;width:164px;height:44px;font-size:13px">Submit now</div>
</div>
<div class="abs map" role="img" aria-label="Street map of the office neighbourhood with a location pin">
  <svg width="453" height="440" style="position:absolute;left:0;top:0"><circle cx="150" cy="170" r="62" fill="none" stroke="#0455a3" stroke-width="2"/><circle cx="150" cy="170" r="38" fill="none" stroke="#0455a3" stroke-width="2"/><circle cx="150" cy="170" r="20" fill="#0455a3"/><circle cx="150" cy="168" r="7" fill="#fff"/></svg>
</div>

<div class="abs logo" style="top:4855px"><span class="mark" style="width:68px;height:68px;background:var(--white)"></span><span><span class="word" style="color:var(--white);font-size:32px">VORSELITH</span><span class="tag" style="color:var(--white)">EFFECTIVE TECHNOLOGY MANAGEMENT</span></span></div>
<p class="abs" style="left:100px;top:4980px;width:400px;font-size:13px;line-height:24px;color:var(--white)">Lorem ipsum dolor sit amet, consectetur adipiscing elit, sed do eiusmod tempor incididunt ut labore et dolore magna aliqua. Quis ipsum suspendisse ultrices gravida.</p>
<span class="fsocial" style="left:100px"></span><span class="fsocial" style="left:150px"></span><span class="fsocial" style="left:200px"></span><span class="fsocial" style="left:250px"></span>

<div class="fhead" style="left:582px">MAIN INFO</div>
<ul class="flinks" style="left:582px"><li>Home</li><li>What We Do</li><li>Resources</li><li>Comany</li><li>Contact Us</li></ul>
<div class="fhead" style="left:778px">OUR SERVICES</div>
<ul class="flinks" style="left:778px"><li>Cloud Adoption</li><li>Managed Services</li><li>Optimise</li></ul>
<div class="fhead" style="left:997px">RESOURCES</div>
<ul class="flinks" style="left:997px"><li>News</li><li>Resources</li><li>Events</li><li>Webinars</li><li>Not for profit</li><li>Case Studies</li></ul>

<div class="abs" style="left:100px;top:5120px;width:1000px;height:1px;background:rgba(255,255,255,.35)"></div>
<div class="abs" style="left:100px;top:5142px;font-size:13px;color:var(--white)">Copyright © 2021 Vorselith. All rights reserved.</div>
<div class="abs" style="left:948px;top:5142px;font-size:13px;color:var(--white)">CONTACT &nbsp;| &nbsp;SUPPORT</div>

</body>
</html>
```